Wine Bottle Lable

Want a unique, simple but elegant, label for a wine bottle. I want to use the letters "TWG" in the design which is a moniker for my last name "Tallwidge". The letters TWG do not have to be juxtaposed together so that it is recognizable, or they could be something like T-WG, WG-T, TGW T-WG-T, etc. The X could be totally separated from the NO, or otherwise. The wine is a white wine in a clear bottle. I need Adobe Illustrator files so I can add the wine varietal, year, alcohol content. The label should be 4" wide and 5" tall.

Colors

Designer to choose colors to be used in the design.

Requirements
Nice to have
• outstanding but simple graphics

```html
<!DOCTYPE html>
<html lang="en">
<head>
<meta charset="utf-8">
<title>TWG White Wine Label – Tallwidge Winery</title>
<link rel="stylesheet" href="https://fonts.googleapis.com/css2?family=Playfair+Display:ital,wght@0,400;1,400&display=swap">
<style>
  :root {
    --backdrop: #efe6da;
    --label-cream: #f7f1e1;
    --label-ink: #2f2f2f;
    --band-dark: #2a2a2a;
    --band-dark-soft: #353535;
    --band-text: #f3ecd8;
    --ornament-tone: #8a8478;
  }
  html, body {
    margin: 0;
    padding: 0;
    width: 957px;
    height: 1200px;
    overflow: hidden;
    background: var(--backdrop);
  }
  .canvas {
    position: relative;
    width: 957px;
    height: 1200px;
  }
  .wine-label {
    position: absolute;
    left: 98px;
    top: 128px;
    width: 760px;
    height: 944px;
    display: block;
  }
  .label-type {
    font-family: "Playfair Display", Georgia, serif;
    font-weight: 400;
  }
  .monogram-t { fill: var(--label-ink); font-size: 800px; }
  .monogram-wg { fill: var(--label-ink); font-size: 170px; }
  .monogram-sub { fill: var(--label-ink); font-size: 88px; }
  .varietal { fill: var(--label-ink); font-size: 84px; }
  .winery-name { fill: var(--band-text); font-size: 36px; }
  .vintage { fill: var(--band-text); font-size: 60px; font-style: italic; }
</style>
</head>
<body>
<main class="canvas">
  <svg class="wine-label" viewBox="0 0 760 944" xmlns="http://www.w3.org/2000/svg" aria-label="TWG white wine label by Tallwidge Winery, 2019">
    <defs>
      <clipPath id="label-shape">
        <rect x="0" y="0" width="760" height="944" rx="28" ry="28"/>
      </clipPath>
      <linearGradient id="band-shade" x1="0" y1="0" x2="1" y2="1">
        <stop offset="0" stop-color="var(--band-dark-soft)"/>
        <stop offset="0.5" stop-color="var(--band-dark)"/>
        <stop offset="1" stop-color="var(--band-dark-soft)"/>
      </linearGradient>
    </defs>

    <g clip-path="url(#label-shape)">
      <rect class="label-face" x="0" y="0" width="760" height="640" fill="var(--label-cream)"/>
      <rect class="label-band" x="0" y="640" width="760" height="304" fill="url(#band-shade)"/>

      <text class="label-type monogram-t" x="-30" y="605">T</text>
      <text class="label-type monogram-wg" x="300" y="365">WG</text>
      <text class="label-type monogram-sub" x="590" y="365">t</text>

      <text class="label-type varietal" transform="translate(654 18) rotate(90)" x="0" y="0" textLength="590" lengthAdjust="spacingAndGlyphs">WHITE WINE</text>

      <g class="band-ornament" role="img" aria-label="Small decorative flourish ornament">
        <rect x="318" y="690" width="124" height="56" rx="28" fill="var(--ornament-tone)" opacity="0.55"/>
      </g>

      <text class="label-type winery-name" x="380" y="812" text-anchor="middle" textLength="565" lengthAdjust="spacing">BY TALLWIDGE WINERY</text>
      <text class="label-type vintage" x="380" y="906" text-anchor="middle" textLength="235" lengthAdjust="spacing">- 2019 -</text>
    </g>

    <rect class="label-edge" x="1.5" y="1.5" width="757" height="941" rx="27" ry="27" fill="none" stroke="var(--band-dark)" stroke-width="3"/>
  </svg>
</main>
</body>
</html>
```